Business Card Design Wenda Style

I make Hand Made Name necklaces which are known as Wenda Style and would like a Shiny Gold Business Card almost to look like a Gold Bar.
on the 2nd side I want an image of a Wenda Necklace in Silver as it will be on a Gold Background.

Industry/Entity Type

Business

Contact Information for Business Card

Dunvok Jewellery UK
Loop Pendants 2 Go

Hugo Penwright
Director
M: 07700 914 263

www.dunvokjwl.co.uk

Requirements
Must have
• Writing must be in Black

Card must be metallic gold

```html
<!DOCTYPE html>
<html lang="en">
<head>
<meta charset="utf-8">
<title>Dunvok Jewellery UK — Business Card</title>
<link rel="stylesheet" href="https://fonts.googleapis.com/css2?family=Alegreya+Sans+SC:ital,wght@1,500&family=Cinzel+Decorative:wght@700&family=Cinzel:wght@600&family=Tenor+Sans&display=swap">
<style>
  :root {
    --backdrop: #e9e4da;
    --gold-deep: #c9952f;
    --gold-mid: #e3bb5c;
    --gold-light: #fbeaae;
    --gold-glow: #fff6d6;
    --silver-dark: #b9b6ae;
    --silver-light: #f4f2ec;
    --ink: #111111;
    --accent-red: #8e1414;
  }
  * { margin: 0; padding: 0; box-sizing: border-box; }
  html, body {
    width: 1200px;
    height: 1200px;
    overflow: hidden;
    background: var(--backdrop);
  }
  .canvas {
    width: 1200px;
    height: 1200px;
    display: flex;
    align-items: center;
    justify-content: center;
  }
  .business-card {
    position: relative;
    width: 1040px;
    height: 650px;
    overflow: hidden;
    background:
      radial-gradient(ellipse 520px 300px at 42% 30%, var(--gold-glow) 0%, rgba(255,246,214,0) 70%),
      linear-gradient(160deg, rgba(255,255,255,0) 38%, rgba(255,250,225,0.7) 50%, rgba(255,255,255,0) 62%),
      linear-gradient(115deg, var(--gold-mid) 0%, var(--gold-light) 35%, var(--gold-mid) 58%, var(--gold-light) 78%, var(--gold-deep) 100%);
    box-shadow: 0 18px 40px rgba(60, 40, 10, 0.25);
  }
  .necklace-photo {
    position: absolute;
    left: 150px;
    top: 0;
    width: 700px;
    height: 280px;
  }
  .brand-block {
    position: absolute;
    left: 70px;
    top: 430px;
    color: var(--ink);
    font-family: "Alegreya Sans SC", sans-serif;
    font-style: italic;
    font-weight: 500;
    line-height: 1.05;
  }
  .brand-name { font-size: 44px; letter-spacing: 0.5px; }
  .brand-tagline { font-size: 58px; letter-spacing: 0.5px; }
  .brand-tagline .accent { color: var(--accent-red); }
  .contact-block {
    position: absolute;
    left: 570px;
    top: 330px;
    width: 400px;
    color: var(--ink);
  }
  .contact-name {
    font-family: "Cinzel", serif;
    font-weight: 600;
    font-size: 34px;
    padding-bottom: 4px;
    border-bottom: 2px solid var(--ink);
  }
  .contact-name .initial {
    font-family: "Cinzel Decorative", serif;
    font-weight: 700;
    font-size: 46px;
  }
  .contact-lines {
    margin-top: 16px;
    font-family: "Tenor Sans", sans-serif;
    font-size: 28px;
    line-height: 1.45;
    letter-spacing: 0.5px;
  }
</style>
</head>
<body>
  <main class="canvas">
    <section class="business-card">
      <svg class="necklace-photo" viewBox="0 0 700 280" role="img" aria-label="Photograph of a silver handmade script name necklace on a fine chain">
        <defs>
          <linearGradient id="silver-fill" x1="0" y1="0" x2="1" y2="1">
            <stop offset="0" stop-color="var(--silver-light)"/>
            <stop offset="0.5" stop-color="var(--silver-dark)"/>
            <stop offset="1" stop-color="var(--silver-light)"/>
          </linearGradient>
        </defs>
        <rect x="40" y="60" width="620" height="190" rx="95" fill="url(#silver-fill)" opacity="0.85"/>
      </svg>

      <div class="brand-block">
        <p class="brand-name">Dunvok Jewellery UK</p>
        <p class="brand-tagline">Loop Pendants <span class="accent">2</span> Go</p>
      </div>

      <div class="contact-block">
        <p class="contact-name"><span class="initial">H</span>ugo Penwright</p>
        <div class="contact-lines">
          <p>DIRECTOR</p>
          <p>MOBILE: 07700 914 263</p>
          <p>WWW.DUNVOKJWL.CO.UK</p>
        </div>
      </div>
    </section>
  </main>
</body>
</html>
```